The Maplewick Academy Web Page

We need a web design for our Day Care Center based in Brandon, Florida. We are targeting child care and educational services to middle class parents, specially the mother. We would like to see designs that matches attached logo mark. The final design should communicate higher standards for day care and educational services.

Target Market(s)

Middle class parents in the State of Florida

Coding

Number of Pages Required

5+ page

```html
<!DOCTYPE html>
<html lang="en">
<head>
<meta charset="utf-8">
<title>The Maplewick Academy</title>
<link href="https://fonts.googleapis.com/css2?family=Roboto:wght@300;400;500&display=swap" rel="stylesheet">
<style>
:root{
  --gold:#d9a23a;
  --gold-dark:#c18c27;
  --navy:#0b1e3f;
  --navy-deep:#071630;
  --text:#4a4a4a;
  --heading:#1b2536;
  --panel:#f3f3f3;
  --line:#d8d8d8;
}
*{margin:0;padding:0;box-sizing:border-box}
html,body{width:699px;height:1200px;overflow:hidden;background:#fff}
body{font-family:'Roboto',sans-serif;color:var(--text);position:relative}
.abs{position:absolute}
.top-links{top:10px;right:43px;font-size:7px;color:#555;font-weight:300}
.top-links span{margin:0 4px;color:#888}
.brand{top:10px;left:43px;display:flex;align-items:center;gap:7px}
.brand-mark{width:26px;height:26px;border-radius:50%;background:var(--navy)}
.brand-name{font-size:12px;font-weight:500;color:var(--navy)}
.search{top:38px;left:499px;width:133px;height:21px;border:1px solid #ddd;background:#f5f5f5;font-size:6.5px;font-style:italic;color:#aaa;padding:7px 8px}
.search-btn{top:38px;left:633px;width:22px;height:21px;background:var(--gold)}
.nav{top:73px;left:0;width:699px;height:28px;background:var(--navy)}
.nav ul{list-style:none;display:flex;position:absolute;left:43px;top:0;height:28px}
.nav li{font-size:7.5px;color:#fff;line-height:28px;text-transform:uppercase;margin-right:31px}
.nav li.active{background:var(--gold);padding:0 10px;margin-right:19px}
.nav li:last-child{margin-right:0}
.hero{top:105px;left:43px;width:613px;height:236px;border:2px solid #ddd;background:linear-gradient(120deg,#c9b49a,#e8d9c6 45%,#b99a7c)}
.hero-caption{position:absolute;left:0;right:0;bottom:0;height:37px;background:rgba(207,152,44,.88);color:#fff;font-size:21px;font-weight:400;padding:5px 15px;letter-spacing:.3px}
.dots{position:absolute;right:10px;top:15px;display:flex;gap:3px}
.dots i{width:7px;height:7px;border-radius:50%;background:#fff}
.dots i:first-child{background:var(--navy)}
h2{font-weight:400;color:var(--heading)}
.welcome-title{top:361px;left:43px;font-size:16px}
.welcome-text{top:385px;left:43px;width:403px;font-size:7.4px;line-height:13px;font-weight:300}
.btn{display:block;width:67px;height:21px;background:var(--gold);color:#fff;font-size:6.5px;font-weight:500;text-align:center;line-height:21px;text-transform:uppercase}
.welcome-btn{top:449px;left:43px}
.welcome-photo{top:366px;left:462px;width:194px;height:104px;background:linear-gradient(135deg,#b48a4e,#d7c39a 50%,#8e6a3c)}
.divider{top:488px;left:43px;width:613px;height:1px;background:var(--line)}
.services-title{top:497px;left:43px;font-size:16px}
.service{top:522px;width:141px}
.service .photo{height:73px;border:2px solid #ccc}
.service h3{font-size:8px;font-weight:500;color:var(--heading);margin-top:10px}
.service p{font-size:7.2px;line-height:13px;font-weight:300;margin-top:2px;height:40px}
.service .btn{margin-top:9px}
.campuses{top:702px;left:43px;width:613px;height:83px;background:var(--navy);color:#fff}
.campuses h2{color:#fff;font-size:16px;position:absolute;left:13px;top:11px}
.campuses p{position:absolute;left:14px;top:34px;width:290px;font-size:6.8px;line-height:13px;font-style:italic;font-weight:300;color:#dfe4ec}
.field{position:absolute;left:320px;width:191px;height:21px;background:#fff;font-size:6.5px;font-style:italic;color:#999;padding:7px 9px}
.find{position:absolute;left:518px;top:20px;width:78px;height:47px;background:var(--gold);color:#fff;font-size:12px;text-align:center;line-height:15px;padding-top:9px;text-transform:uppercase}
.box{top:800px;width:192px;height:200px;background:var(--panel)}
.box h2{font-size:16px;position:absolute;left:11px;top:9px}
.box .photo{position:absolute;left:11px;top:30px;width:171px;height:87px}
.box p{position:absolute;left:11px;top:124px;width:175px;font-size:7.2px;line-height:13px;font-weight:300}
.box .btn{position:absolute;left:11px;top:168px}
.footer{top:1017px;left:0;width:699px;height:144px;background:linear-gradient(180deg,#0e2246,#0c2a5e)}
.fcol{position:absolute;top:27px}
.fcol h4{font-size:9.5px;font-weight:400;color:var(--gold);margin-bottom:5px}
.fcol li{list-style:none;font-size:6px;color:#c3cbd8;line-height:15.6px;font-weight:300}
.bottom{top:1161px;left:0;width:699px;height:39px;background:var(--navy-deep)}
.copy{position:absolute;left:43px;top:17px;font-size:6px;color:#8a96ab;font-weight:300}
.social{position:absolute;right:43px;top:11px;display:flex;gap:4px}
.social i{width:17px;height:17px;border-radius:50%;background:#2f4a78}
</style>
</head>
<body>
<div class="abs top-links">Preferred Vendors<span>/</span>Real Estate<span>/</span>Business Co-Ops<span>/</span>Career Opportunities<span>/</span>Privacy Policy<span>/</span>Franchise Privacy Policy</div>
<div class="abs brand"><div class="brand-mark"></div><div class="brand-name">The Maplewick Academy</div></div>
<div class="abs search">Search...</div>
<div class="abs search-btn"><svg width="22" height="21" viewBox="0 0 22 21"><circle cx="10" cy="9" r="4" fill="none" stroke="#fff" stroke-width="1.6"/><line x1="13" y1="12" x2="16" y2="15" stroke="#fff" stroke-width="2"/></svg></div>
<nav class="abs nav"><ul><li class="active">Home</li><li>Admissions</li><li>Philosophy</li><li>Programs</li><li>Services</li><li>Campuses</li><li>Franchises</li><li>Business</li><li>Contact</li></ul></nav>
<div class="abs hero" role="img" aria-label="Photo of a mother reading a book with a group of young children">
  <div class="hero-caption">We Are a Day Care Center for Kids<div class="dots"><i></i><i></i><i></i><i></i></div></div>
</div>
<h2 class="abs welcome-title">Welcome to Our Website</h2>
<p class="abs welcome-text">Aliquam molestie, mi et imperdiet euismod, dui purus auctor tellus, et interdum lacus lectus et ante. Sed accumsan sollicitudin sapien, sit amet adipiscing turpis gravida ac. In congue, neque ac lobortis volutpat, libero mauris varius mi, vitae suscipit ipsum ligula vitae risus. Duis aliquam nibh a dui iaculis viverra id a velit. Vivamus egestas risus in magna varius commodo. Sed semper viverra egestas...</p>
<a class="abs btn welcome-btn">Read More</a>
<div class="abs welcome-photo" role="img" aria-label="Photo of smiling children with a teacher at a play table"></div>
<div class="abs divider"></div>
<h2 class="abs services-title">Our Services</h2>
<div class="abs service" style="left:43px"><div class="photo" role="img" aria-label="Photo of a mother helping a child with homework" style="background:linear-gradient(135deg,#d8cfc6,#a88b76)"></div><h3>Home School Support</h3><p>Aliquam molestie, mi et imperdiet euismod, dui purus auctor tellus, et interdum lacus lectus et ante.</p><a class="btn">Read More</a></div>
<div class="abs service" style="left:199px"><div class="photo" role="img" aria-label="Photo of school children on a yellow background" style="background:linear-gradient(135deg,#f3b21a,#e5713a)"></div><h3>School Readiness Provider</h3><p>Aliquam molestie, mi et imperdiet euismod, dui purus auctor tellus, et interdum lacus lectus et ante.</p><a class="btn">Read More</a></div>
<div class="abs service" style="left:358px"><div class="photo" role="img" aria-label="Photo of a teacher with pre-K pupils raising hands" style="background:linear-gradient(135deg,#8a8f96,#d8d4cf)"></div><h3>Voluntary Pre-K (VPK)</h3><p>Aliquam molestie, mi et imperdiet euismod, dui purus auctor tellus, et interdum lacus lectus et ante.</p><a class="btn">Read More</a></div>
<div class="abs service" style="left:515px"><div class="photo" role="img" aria-label="Photo of happy children jumping outdoors" style="background:linear-gradient(180deg,#a9cde8,#e8a35a)"></div><h3>Enrichment Services</h3><p>Aliquam molestie, mi et imperdiet euismod, dui purus auctor tellus, et interdum lacus lectus et ante.</p><a class="btn">Read More</a></div>
<section class="abs campuses">
  <h2>Campuses</h2>
  <p>Enter contact email and Enter Zip Code to find a Center near you. Show a map with the location. If school is not available. (There is no Campus available in this area yet. Would like us to contact you once it becomes available?)</p>
  <div class="field" style="top:20px">Enter Email Address</div>
  <div class="field" style="top:47px">Enter Zip Code</div>
  <div class="find">Find a<br>Center</div>
</section>
<div class="abs box" style="left:43px"><h2>Philosophy</h2><div class="photo" role="img" aria-label="Photo of a teacher reading with a boy" style="background:linear-gradient(135deg,#3b3531,#a89780)"></div><p>Aliquam molestie, mi et imperdiet euismod, dui purus auctor tellus, et interdum lacus lectus et ante nibh eget turpis vehiculat..</p><a class="btn">Read More</a></div>
<div class="abs box" style="left:253px"><h2>Admission</h2><div class="photo" role="img" aria-label="Photo of a girl reading a yellow book" style="background:linear-gradient(135deg,#cfe3ec,#e8b84a)"></div><p>Aliquam molestie, mi et imperdiet euismod, dui purus auctor tellus, et interdum lacus lectus et ante nibh eget turpis vehiculat..</p><a class="btn">Read More</a></div>
<div class="abs box" style="left:463px"><h2>Programs</h2><div class="photo" role="img" aria-label="Photo of children playing in a colourful play area" style="background:linear-gradient(135deg,#e24a35,#f0a0b0 55%,#4ca04a)"></div><p>Aliquam molestie, mi et imperdiet euismod, dui purus auctor tellus, et interdum lacus lectus et ante nibh eget turpis vehiculat..</p><a class="btn">Read More</a></div>
<footer class="abs footer">
  <div class="fcol" style="left:43px"><h4>Admissions</h4><ul><li>Apply for Admission</li><li>Schedule a Campus Tour</li><li>Enrollment Policy</li></ul></div>
  <div class="fcol" style="left:148px"><h4>Philosophy</h4><ul><li>Values</li><li>Mission</li><li>Vision</li><li>Purpose</li><li>Advantage</li><li>Curriculum</li></ul></div>
  <div class="fcol" style="left:236px"><h4>Programs</h4><ul><li>Children from 1 – 2 Years</li><li>Children from 2 – 3 Years</li><li>Children from 3 – 4 years</li><li>Children from 4 - 5 Years</li><li>Voluntary Pre-K (VPK)</li><li>Kindergarten</li></ul></div>
  <div class="fcol" style="left:341px"><h4>&nbsp;</h4><ul><li>1s Grade</li><li>2nd Grade</li><li>3rd Grade</li><li>4th Grade</li><li>5th Grade</li></ul></div>
  <div class="fcol" style="left:412px"><h4>Services</h4><ul><li>Home School Support</li><li>School Readiness Provider</li><li>Voluntary Pre-K (VPK)</li><li>Enrichment Services</li></ul></div>
  <div class="fcol" style="left:516px"><h4>Franchises</h4><ul><li>About The Maplewick Academy</li><li>Our Advantage</li><li>Contact Us</li></ul></div>
</footer>
<div class="abs bottom">
  <div class="copy">Copyright © 2015. CompanyName. All Right Reserved &nbsp;|&nbsp; Privacy Policy</div>
  <div class="social"><i></i><i></i><i></i><i></i><i></i><i></i></div>
</div>
</body>
</html>
```